Website design for an existing WordPress theme

Looking to get an experienced designer to help design a renewed informative website for a company in the field of digital sports media.

The website is already built using WordPress with a theme called "Marquee" from LayoutBazaar:
http://layoutbazaar.example/item/marquee-premium-multipurpose-wordpress-theme/3016482

We simply require to complete the graphic design, including:

* Taking our logo colors into consideration.
* Setting a Color Scheme.
* Typographical hierarchy - fonts and sizes (based on Google fonts)
* Background images
* Design for information boxes (if needed)

The website includes only 3-4 main pages:
1) Home page - including concept and product description - this requires the most design work.
2) Technology - short information page - needs some images.
3) About / Team - a short paragraph about the company and small biography paragraphs about each of the founders.
4) Contact us form

Check out the existing page here: http://www.plorvexa.example/wordpress/

Redesign the existing informational website.
Notice the logo colors.

An example website:
http://www.glintreel.example/corp/
Maybe with sports pictures in the background, but we're not sure about it.

We also need the main image, on the top of the page - redesigned and adapted.
An image characterizing this main explanatory image is attached to this project description.

```html
<!DOCTYPE html>
<html lang="en">
<head>
<meta charset="utf-8">
<title>Plorvexa – Take The Lead</title>
<link href="https://fonts.googleapis.com/css2?family=Questrial&family=Arimo:wght@400;700&display=swap" rel="stylesheet">
<style>
:root{
  --bar:#232323;
  --dark:#2a2a2a;
  --footer:#2e2e2e;
  --white:#ffffff;
  --muted:#9a9a9a;
  --text-dark:#444444;
  --gold-top:#f8cd4a;
  --gold-bot:#efb21e;
  --gold-edge:#d39a14;
  --gold-ink:#8a5b05;
  --teal:#1fb59b;
  --tick:#8cc63f;
  --link:#2a6fb5;
  --line:#444444;
}
*{margin:0;padding:0;box-sizing:border-box}
html,body{width:718px;height:1200px;overflow:hidden}
body{position:relative;background:var(--white);font-family:"Arimo",Arial,sans-serif;color:var(--white)}
h2,h3{font-weight:400}
.abs{position:absolute}
.display{font-family:"Questrial",Arial,sans-serif;font-weight:400}

.site-header{left:0;top:0;width:718px;height:42px;background:var(--bar)}
.brand{left:103px;top:7px;display:flex;align-items:center;gap:6px}
.brand-mark{width:28px;height:28px;border-radius:50%;background:#e8a623}
.brand-name{font-family:"Questrial",sans-serif;font-size:13px;color:var(--white)}
.brand-tag{font-family:"Questrial",sans-serif;font-size:13px;color:var(--white);margin-left:4px}
.main-nav{top:18px;font-size:7.5px;color:#bdbdbd}

.hero{left:0;top:42px;width:718px;height:288px;
  background:radial-gradient(ellipse at 45% 40%,#8a6a2e 0%,#4a3518 40%,#1d140a 80%),#2a1d0e}
.hero-diagram{left:0;top:42px}
.hero-label{font-size:7.3px;color:var(--white);text-align:center}
.hero-label.right{text-align:left}

.strategy-title{left:0;width:718px;top:362px;text-align:center;font-size:11.5px;color:var(--text-dark);letter-spacing:.1px}
.gold-btn{height:26px;border:1px solid var(--gold-edge);background:linear-gradient(var(--gold-top),var(--gold-bot));
  color:var(--gold-ink);font-family:"Questrial",sans-serif;font-size:9px;display:flex;align-items:center;justify-content:center}

.production{left:0;top:454px;width:718px;height:346px;background:var(--dark)}
.prod-title{left:0;width:718px;top:481px;text-align:center;font-size:11.5px}
.prod-copy{left:0;width:718px;top:505px;text-align:center;font-size:6.6px;line-height:14.4px;color:#e6e6e6}
.divider{left:102px;top:562px;width:514px;height:1px;background:var(--line)}
.media{border-radius:2px}
.feature-logo{display:flex;align-items:center;gap:5px}
.feature-logo .sq{width:14px;height:14px;background:var(--teal)}
.feature-logo span{font-family:"Questrial",sans-serif;font-size:17px;color:var(--teal);letter-spacing:1px}
.feature-title{font-size:11px}
.ticks{list-style:none;width:260px}
.ticks li{position:absolute;left:0;padding-left:17px;font-size:7.2px;line-height:14px;width:260px}
.ticks svg{position:absolute;left:0;top:2px}
.on-dark li{color:#f0f0f0}
.on-light li{color:#555}
.view-next{width:66px;height:66px;border-radius:50%;text-align:center;font-size:6.4px;color:var(--link)}
.view-next p{margin-top:26px}
.view-next.solid{background:var(--white)}
.view-next.outline{border:1px solid #bbb;background:var(--white)}

.site-footer{left:0;top:1152px;width:718px;height:48px;background:var(--footer);font-size:6.4px;color:var(--muted)}
.social{width:18px;height:18px;border-radius:50%;background:#7a7a7a;top:15px}
</style>
</head>
<body>

<header class="site-header abs">
  <div class="brand abs"><div class="brand-mark"></div><span class="brand-name">Plorvexa</span><span class="brand-tag">Take The Lead</span></div>
  <nav>
    <span class="main-nav abs" style="left:470px">Home</span>
    <span class="main-nav abs" style="left:524px">About</span>
    <span class="main-nav abs" style="left:579px">Contact Us</span>
  </nav>
</header>

<section class="hero abs" role="img" aria-label="Basketball player reaching toward the hoop on a warm-lit court"></section>

<svg class="hero-diagram abs" width="718" height="288" viewBox="0 42 718 288" fill="none" stroke="#fff" stroke-width="2">
  <path d="M53 167 L46 184 L53 201" stroke-width="1" stroke="#ccc"/>
  <path d="M665 167 L672 184 L665 201" stroke-width="1" stroke="#ccc"/>
  <circle cx="198" cy="186" r="28"/>
  <circle cx="321" cy="186" r="28"/>
  <circle cx="470" cy="107" r="28"/>
  <circle cx="470" cy="185" r="28"/>
  <circle cx="470" cy="262" r="28"/>
  <path d="M234 186 H283 M277 181 L284 186 L277 191"/>
  <path d="M364 185 H430 M424 180 L431 185 L424 190"/>
  <path d="M364 165 C395 168 418 150 428 126 M421 129 L429 124 L431 133"/>
  <path d="M364 203 C395 200 418 218 428 240 M421 237 L429 242 L431 233"/>
  <g fill="#fff" stroke="none">
    <rect x="188" y="171" width="14" height="10" rx="1"/>
    <path d="M202 176 L209 172 V180 Z"/>
    <rect x="190" y="185" width="16" height="16" rx="1"/>
  </g>
  <rect x="193" y="188" width="10" height="4" fill="#222" stroke="none"/>
  <rect x="193" y="194" width="10" height="4" fill="#222" stroke="none"/>
  <g stroke-width="1.6">
    <rect x="311" y="174" width="12" height="18" transform="rotate(-25 317 183)" fill="#fff"/>
    <circle cx="330" cy="193" r="3"/><circle cx="336" cy="188" r="3"/>
    <path d="M332 191 L325 183 M334 190 L328 181"/>
  </g>
  <g fill="#fff" stroke="none">
    <rect x="462" y="95" width="22" height="10"/>
    <path d="M456 108 h6 v-8 a2 2 0 0 1 4 0 v10 h8 v10 a4 4 0 0 1 -4 4 h-10 Z"/>
  </g>
  <g stroke-width="1.4">
    <rect x="460" y="174" width="20" height="22"/>
    <path d="M464 180 h12 M464 185 h12 M464 190 h12"/>
  </g>
  <g stroke-width="1.6">
    <rect x="458" y="252" width="24" height="18" rx="2"/>
    <path d="M467 256 L476 261 L467 266 Z" fill="#fff"/>
  </g>
</svg>
<div class="hero-label abs" style="left:158px;top:224px;width:80px">Live Sports</div>
<div class="hero-label abs" style="left:276px;top:224px;width:90px;line-height:13.6px">Automatic editing in<br>real-time</div>
<div class="hero-label right abs" style="left:509px;top:102px">For Engagement</div>
<div class="hero-label right abs" style="left:509px;top:180px">Sports articles</div>
<div class="hero-label right abs" style="left:509px;top:257px">Video Platforms</div>

<h2 class="strategy-title display abs">CHECK OUT HOW WE CAN HELP YOUR DIGITAL SPORTS STRATEGY</h2>
<div class="gold-btn abs" style="left:126px;top:394px;width:143px">PRODUCTION</div>
<div class="gold-btn abs" style="left:288px;top:394px;width:143px">EDITORIAL</div>
<div class="gold-btn abs" style="left:449px;top:394px;width:143px">FAN ENGAGEMENT</div>

<section class="production abs"></section>
<h2 class="prod-title display abs">PRODUCTION – CONTROL AND CURATE YOUR VIDEOS</h2>
<div class="prod-copy abs">
  Use our AutoForge and Reelcut tools to automate most of your production workload.<br>
  Our system tags every event, creates both in-game and post-game highlight packages and also shares every type of media to digital platforms, social media and OVPs.<br>
  We help you stay in control and focus on making sure the best content is created, curated and pushed to the right place at the right time.
</div>
<div class="divider abs"></div>

<div class="media abs" style="left:102px;top:591px;width:226px;height:158px;background:linear-gradient(#b9a98a,#8a6f9a 60%,#2c2c2c)" role="img" aria-label="Video player showing a basketball game highlight"></div>

<div class="feature-logo abs" style="left:356px;top:596px"><div class="sq"></div><span>REELCUT</span></div>
<h3 class="feature-title display abs" style="left:357px;top:636px">AUTOMATIC VIDEO GENERATION</h3>
<ul class="ticks on-dark abs" style="left:358px;top:658px">
  <li style="top:0"><svg width="10" height="9" viewBox="0 0 10 9"><path d="M1 5 L4 8 L9 1" stroke="#8cc63f" stroke-width="2" fill="none"/></svg>Automatic generation of in-game, post-game and archive highlight packages</li>
  <li style="top:18px"><svg width="10" height="9" viewBox="0 0 10 9"><path d="M1 5 L4 8 L9 1" stroke="#8cc63f" stroke-width="2" fill="none"/></svg>Dynamic video intros created on the fly according to the content of the clips.</li>
  <li style="top:40px"><svg width="10" height="9" viewBox="0 0 10 9"><path d="M1 5 L4 8 L9 1" stroke="#8cc63f" stroke-width="2" fill="none"/></svg>Management system to enable you to control what types of clips will be created and when.</li>
  <li style="top:82px"><svg width="10" height="9" viewBox="0 0 10 9"><path d="M1 5 L4 8 L9 1" stroke="#8cc63f" stroke-width="2" fill="none"/></svg>Distribution and publishing control to digital, social and OVPs</li>
</ul>

<div class="view-next solid abs" style="left:325px;top:776px">
  <p>VIEW NEXT</p>
  <svg width="10" height="6" viewBox="0 0 10 6"><path d="M1 1 L5 5 L9 1" stroke="#555" stroke-width="1.2" fill="none"/></svg>
</div>

<div class="media abs" style="left:109px;top:852px;width:214px;height:196px;background:linear-gradient(#1b1b1b 0,#3a3a3a 70%,#d8d8d8 80%,#ffffff 100%)" role="img" aria-label="Desktop monitor displaying the cloud production player"></div>

<div class="feature-logo abs" style="left:358px;top:850px"><div class="sq"></div><span>REELCUT</span></div>
<h3 class="feature-title display abs" style="left:359px;top:889px;color:#333">CLOUD-BASED PRODUCTION</h3>
<ul class="ticks on-light abs" style="left:358px;top:912px">
  <li style="top:0"><svg width="10" height="9" viewBox="0 0 10 9"><path d="M1 5 L4 8 L9 1" stroke="#8cc63f" stroke-width="2" fill="none"/></svg>Automatic generation of in-game, post-game and archive highlight packages</li>
  <li style="top:18px"><svg width="10" height="9" viewBox="0 0 10 9"><path d="M1 5 L4 8 L9 1" stroke="#8cc63f" stroke-width="2" fill="none"/></svg>Dynamic video intros created on the fly according to the content of the clips.</li>
  <li style="top:40px"><svg width="10" height="9" viewBox="0 0 10 9"><path d="M1 5 L4 8 L9 1" stroke="#8cc63f" stroke-width="2" fill="none"/></svg>Management system to enable you to control what types of clips will be created and when.</li>
  <li style="top:72px"><svg width="10" height="9" viewBox="0 0 10 9"><path d="M1 5 L4 8 L9 1" stroke="#8cc63f" stroke-width="2" fill="none"/></svg>Distribution and publishing control to digital, social and OVPs</li>
</ul>
<div class="gold-btn abs" style="left:359px;top:1009px;width:92px;height:24px">VIEW DEMO</div>

<div class="view-next outline abs" style="left:325px;top:1058px">
  <p>VIEW NEXT</p>
  <svg width="10" height="6" viewBox="0 0 10 6"><path d="M1 1 L5 5 L9 1" stroke="#555" stroke-width="1.2" fill="none"/></svg>
</div>

<footer class="site-footer abs">
  <span class="abs" style="left:103px;top:21px">© All Rights Reserved To Plorvexa Sports Technologies 2014</span>
  <span class="abs" style="left:452px;top:21px">Follow Us :</span>
  <span class="social abs" style="left:489px"></span>
  <span class="social abs" style="left:511px"></span>
  <span class="social abs" style="left:532px"></span>
  <span class="social abs" style="left:554px"></span>
  <span class="social abs" style="left:576px"></span>
  <span class="social abs" style="left:597px"></span>
</footer>

</body>
</html>
```